Wine Label: Tressivo

The project is to create 3 wine labels. The brand name is "Tressivo"

What we need is to have 3 versions: red wine, white wine and rose.

The wine is for young and modern people, between 21 and 31 years old, so it need to be casual, modern and fun, but at the same time it needs to keep the Premiums of a good European wine.

It is from Italy.

Target Market(s)

Young adults, between 21 and 31 years old. wine lovers

Requirements
Must have
• - Modern colors (Black, silver, red, etc.)
• - Clean label
• - Clear font
• - Style
• - The brand + the type of wine (red, white or rose)
Nice to have
• - A symbol to represent the brand
Should not have
• - Many elements
• - No clear fonts
• - No funny colors

```html
<!DOCTYPE html>
<html lang="en">
<head>
<meta charset="utf-8">
<title>Tressivo Wine Labels</title>
<link rel="stylesheet" href="https://fonts.googleapis.com/css2?family=Cinzel:wght@400&family=Josefin+Sans:wght@400&family=Kaushan+Script&display=swap">
<style>
  :root {
    --page: #ffffff;
    --white-bg: #000000;
    --white-ink: #e6e7e9;
    --red-bg: #5e0006;
    --red-ink: #c09566;
    --rose-bg: #b5151b;
    --rose-ink: #ffffff;
  }
  html, body {
    margin: 0;
    padding: 0;
    overflow: hidden;
  }
  body {
    width: 1200px;
    height: 1080px;
    background: var(--page);
    position: relative;
  }
  .label-set {
    position: absolute;
    left: 252px;
    top: 12px;
    width: 695px;
    display: flex;
    flex-direction: column;
    gap: 24px;
  }
  .wine-label {
    display: block;
    width: 695px;
    height: 336px;
  }
  .wine-label--white { --bg: var(--white-bg); --ink: var(--white-ink); }
  .wine-label--red   { --bg: var(--red-bg);   --ink: var(--red-ink); }
  .wine-label--rose  { --bg: var(--rose-bg);  --ink: var(--rose-ink); }
  .label-bg { fill: var(--bg); }
  .band, .rule, .brand-square { fill: var(--ink); }
  .tagline {
    fill: var(--ink);
    font-family: "Josefin Sans", sans-serif;
    font-size: 9.5px;
    letter-spacing: 2.6px;
  }
  .brand-name {
    fill: var(--ink);
    font-family: "Cinzel", serif;
    font-size: 17px;
    letter-spacing: 0.5px;
  }
  .wine-type {
    fill: var(--ink);
    font-family: "Kaushan Script", cursive;
    font-size: 32px;
  }
</style>
</head>
<body>
<main class="label-set">

  <svg class="wine-label wine-label--white" viewBox="0 0 579 280" aria-label="Tressivo white wine label">
    <rect class="label-bg" width="579" height="280"/>
    <text class="tagline" x="254" y="32">Tressivo&#160;&#160;&#160;&#160;Tressivo&#160;&#160;&#160;&#160;Tressivo</text>
    <rect class="band" x="6" y="48" width="40" height="16"/>
    <rect class="band" x="215" y="48" width="356" height="16"/>
    <rect class="rule" x="6" y="68" width="40" height="2"/>
    <rect class="rule" x="215" y="68" width="356" height="2"/>
    <rect class="rule" x="6" y="207" width="40" height="2"/>
    <rect class="rule" x="215" y="207" width="356" height="2"/>
    <rect class="band" x="6" y="217" width="40" height="15"/>
    <rect class="band" x="215" y="217" width="356" height="15"/>
    <text class="tagline" x="254" y="254">Tressivo&#160;&#160;&#160;&#160;Tressivo&#160;&#160;&#160;&#160;Tressivo</text>
    <rect class="brand-square" x="74" y="133" width="9" height="9"/>
    <text class="brand-name" x="92" y="144">Tressivo</text>
    <text class="wine-type" x="396" y="148" text-anchor="middle">white wine</text>
  </svg>

  <svg class="wine-label wine-label--red" viewBox="0 0 579 280" aria-label="Tressivo red wine label">
    <rect class="label-bg" width="579" height="280"/>
    <text class="tagline" x="254" y="32">Tressivo&#160;&#160;&#160;&#160;Tressivo&#160;&#160;&#160;&#160;Tressivo</text>
    <rect class="band" x="6" y="48" width="40" height="16"/>
    <rect class="band" x="215" y="48" width="356" height="16"/>
    <rect class="rule" x="6" y="68" width="40" height="2"/>
    <rect class="rule" x="215" y="68" width="356" height="2"/>
    <rect class="rule" x="6" y="207" width="40" height="2"/>
    <rect class="rule" x="215" y="207" width="356" height="2"/>
    <rect class="band" x="6" y="217" width="40" height="15"/>
    <rect class="band" x="215" y="217" width="356" height="15"/>
    <text class="tagline" x="254" y="254">Tressivo&#160;&#160;&#160;&#160;Tressivo&#160;&#160;&#160;&#160;Tressivo</text>
    <rect class="brand-square" x="74" y="133" width="9" height="9"/>
    <text class="brand-name" x="92" y="144">Tressivo</text>
    <text class="wine-type" x="396" y="148" text-anchor="middle">red wine</text>
  </svg>

  <svg class="wine-label wine-label--rose" viewBox="0 0 579 280" aria-label="Tressivo rosé label">
    <rect class="label-bg" width="579" height="280"/>
    <text class="tagline" x="254" y="32">Tressivo&#160;&#160;&#160;&#160;Tressivo&#160;&#160;&#160;&#160;Tressivo</text>
    <rect class="band" x="6" y="48" width="40" height="16"/>
    <rect class="band" x="215" y="48" width="356" height="16"/>
    <rect class="rule" x="6" y="68" width="40" height="2"/>
    <rect class="rule" x="215" y="68" width="356" height="2"/>
    <rect class="rule" x="6" y="207" width="40" height="2"/>
    <rect class="rule" x="215" y="207" width="356" height="2"/>
    <rect class="band" x="6" y="217" width="40" height="15"/>
    <rect class="band" x="215" y="217" width="356" height="15"/>
    <text class="tagline" x="254" y="254">Tressivo&#160;&#160;&#160;&#160;Tressivo&#160;&#160;&#160;&#160;Tressivo</text>
    <rect class="brand-square" x="74" y="133" width="9" height="9"/>
    <text class="brand-name" x="92" y="144">Tressivo</text>
    <text class="wine-type" x="396" y="148" text-anchor="middle">rose</text>
  </svg>

</main>
</body>
</html>
```